Halcyon Motion a Centre Pty Ltd

Business card is to promote and represent our new business. It's situated in
48 Wren Parade
Brookvale 2100 Sydney
Our clinic is all about getting people back to great health giving them back their lifestyle in half the usual time it takes to get results elsewhere , we do this through innovative therapies with latest state of the art equipment ,skills ,knowledge and experience.
We give them back their pain free healthy lifestyle with lots of energy to love life and perform their best Quickly and effectively .
The final design should communicate
Trust , confidence, results .

Reason: Waiting for some designers to submit work Thanks

Target Market(s)

High end clients that take their health and results seriously ,
High end athletes , as well as general people that want to see results with different
Treatment Methods and approach

Industry/Entity Type

Clinic

Contact Information for Business Card

Halcyon Motion Centre Pty Ltd
48 Wren Parade Brookvale 2100 Sydney
Website www.halcyonmotioncentre.com.au

Font styles to use
Other font styles liked:
• Gothic font medium

Requirements
Must have
• A designe that makes people look twice with a wow factor , a designe that isn't like all the rest .
• Must have the logo in the colours Iv provided in my files
• Must communicate Trust, confidence , results
Nice to have
• 1) The logo raised up or
• 2) Maybe a pop up logo on the card ?
• Or let's be creative and have two cards one on top of the other so the two cards slide .... The front will have the halcyon logo with the address details etc
• The other card with have
• eg your next app .......................................repeating all way down the card
Should not have
• Basic plain looking card that everyone else has

```html
<!DOCTYPE html>
<html lang="en">
<head>
<meta charset="utf-8">
<title>Halcyon Motion Centre – Business Card</title>
<link rel="stylesheet" href="https://fonts.googleapis.com/css2?family=Oswald:wght@400;500&display=swap">
<style>
  :root {
    --page-bg: #e9ebee;
    --card-bg: #ffffff;
    --brand-green: #5cae3a;
    --brand-blue: #2a6fc4;
    --brand-blue-light: #3fa3e3;
    --brand-navy: #2c3f8f;
    --ink: #2b2b2b;
    --rule: #9a9a9a;
  }
  * { box-sizing: border-box; margin: 0; padding: 0; }
  html, body { width: 1200px; height: 900px; overflow: hidden; }
  body {
    background: var(--page-bg);
    font-family: "Oswald", "Arial Narrow", sans-serif;
    color: var(--ink);
    position: relative;
  }
  .card {
    position: absolute;
    left: 75px; top: 150px;
    width: 1050px; height: 600px;
    background: var(--card-bg);
    border-radius: 60px;
    overflow: hidden;
    box-shadow: 0 14px 40px rgba(0,0,0,.18);
  }
  .card-decor { position: absolute; inset: 0; width: 100%; height: 100%; }
  .brand {
    position: absolute;
    left: 420px; top: 120px;
    display: flex; align-items: center; gap: 22px;
  }
  .brand-dot {
    width: 70px; height: 70px; border-radius: 50%;
    background: var(--brand-green);
  }
  .brand-name {
    font-weight: 500;
    color: var(--brand-navy);
    line-height: 1;
  }
  .brand-name .primary { display: block; font-size: 76px; letter-spacing: 1px; }
  .brand-name .secondary { display: block; font-size: 22px; letter-spacing: 9px; margin-top: 6px; text-transform: uppercase; }
  .contact {
    position: absolute;
    left: 260px; top: 330px;
    display: flex; gap: 30px;
    text-transform: uppercase;
    font-weight: 400;
    font-size: 19px;
    letter-spacing: .5px;
  }
  .person { width: 300px; text-align: right; }
  .person-name { font-size: 22px; font-weight: 500; }
  .person-role { margin-top: 4px; }
  .person-address { margin-top: 44px; line-height: 1.35; }
  .divider { width: 2px; height: 190px; background: var(--rule); }
  .channels { list-style: none; line-height: 1; }
  .channels li { display: flex; align-items: center; gap: 12px; height: 28px; }
  .channels li.gap { margin-top: 14px; }
  .channel-icon { width: 20px; height: 20px; flex: none; }
</style>
</head>
<body>
  <main class="card">
    <svg class="card-decor" viewBox="0 0 1050 600" aria-hidden="true">
      <defs>
        <linearGradient id="blueBand" x1="0" y1="0" x2="1" y2="1">
          <stop offset="0" stop-color="var(--brand-navy)"/>
          <stop offset=".6" stop-color="var(--brand-blue)"/>
          <stop offset="1" stop-color="var(--brand-blue-light)"/>
        </linearGradient>
      </defs>
      <path d="M0,0 H95 C25,180 40,430 230,600 H0 Z" fill="url(#blueBand)"/>
      <path d="M330,600 C600,585 860,560 1050,490 V600 Z" fill="url(#blueBand)"/>
      <path d="M140,0 C60,200 100,460 350,600" fill="none" stroke="var(--brand-green)" stroke-width="9" stroke-linecap="round"/>
    </svg>

    <div class="brand">
      <span class="brand-dot"></span>
      <div class="brand-name">
        <span class="primary">Halcyon</span>
        <span class="secondary">Motion Centre</span>
      </div>
    </div>

    <section class="contact">
      <div class="person">
        <p class="person-name">Mara Ellison</p>
        <p class="person-role">Owner / C.E.O</p>
        <p class="person-address">48 Wren Parade, Brookvale<br>2100</p>
      </div>
      <div class="divider"></div>
      <ul class="channels">
        <li>
          <svg class="channel-icon" viewBox="0 0 20 20"><circle cx="10" cy="10" r="10" fill="var(--ink)"/><path d="M6.5 5.5l2 0 1 2.5-1.3 1c.6 1.3 1.5 2.2 2.8 2.8l1-1.3 2.5 1v2c-4.5.3-8.3-3.5-8-8z" fill="#fff"/></svg>
          02 9905 4417
        </li>
        <li>
          <svg class="channel-icon" viewBox="0 0 20 20"><circle cx="10" cy="10" r="10" fill="var(--ink)"/><rect x="7" y="4.5" width="6" height="11" rx="1" fill="#fff"/><rect x="8" y="6" width="4" height="7" fill="var(--ink)"/></svg>
          0412 386 509
        </li>
        <li>
          <svg class="channel-icon" viewBox="0 0 20 20"><circle cx="10" cy="10" r="10" fill="var(--ink)"/><rect x="5" y="8" width="10" height="6" fill="#fff"/><rect x="7" y="5" width="6" height="3" fill="#fff"/></svg>
          02 9905 4418
        </li>
        <li class="gap">
          <svg class="channel-icon" viewBox="0 0 20 20"><circle cx="10" cy="10" r="10" fill="var(--ink)"/><rect x="5" y="6.5" width="10" height="7" fill="#fff"/><path d="M5 6.5l5 4 5-4" fill="none" stroke="var(--ink)" stroke-width="1.2"/></svg>
          hello@halcyonmotion.com.au
        </li>
        <li>
          <svg class="channel-icon" viewBox="0 0 20 20"><circle cx="10" cy="10" r="10" fill="var(--ink)"/><g fill="none" stroke="#fff" stroke-width="1.2"><circle cx="10" cy="10" r="5.5"/><ellipse cx="10" cy="10" rx="2.3" ry="5.5"/><path d="M4.5 10h11"/></g></svg>
          www.halcyonmotioncentre.com.au
        </li>
      </ul>
    </section>
  </main>
</body>
</html>
```